Medical Practice Business Card

we need a business card for our new medical ophthalmology practice based in Needham Massachusetts. we are looking for a simple , modern and elegant design.
the card needs to contain the following
1- the logo of our practice (please see attached file)
2- the name of the practice : "Silver Birch Retina Care"
3- Doctor's Name: Tobias Rendell MD PhD
4- Specialty: Board-Certified Vitreoretinal Surgeon
5- practice address: 87 Larkspur Ave, Suite 210, Needham MA 02481
7- Office number: 617- 482 - 7730
8- fax number: 617- 391 - 2268
9- email: info@sbretinahub.example
10- website: www.sbretinahub.example

```html
<!DOCTYPE html>
<html lang="en">
<head>
<meta charset="utf-8">
<title>Silver Birch Retina Care — Business Card</title>
<link href="https://fonts.googleapis.com/css2?family=Poppins:wght@500;600&display=swap" rel="stylesheet">
<style>
  :root {
    --page-bg: #f4f5f7;
    --card-bg: #ffffff;
    --navy: #1c3b6a;
    --blue: #2f7fc4;
    --ink: #111111;
    --accent: #6fd0e0;
  }
  * { box-sizing: border-box; margin: 0; padding: 0; }
  html, body {
    width: 1200px; height: 900px; overflow: hidden;
    background: var(--page-bg);
    font-family: "Poppins", sans-serif;
  }
  .card {
    position: absolute; top: 308px;
    width: 499px; height: 289px;
    background: var(--card-bg);
  }
  .card--front { left: 71px; }
  .card--back { left: 635px; }

  .practice-mark {
    position: absolute;
    display: flex; align-items: center; gap: 10px;
    color: var(--navy); font-weight: 600; line-height: 1.15;
  }
  .practice-mark__dot {
    flex: none; border-radius: 50%; background: var(--accent);
  }
  .card--front .practice-mark { left: 300px; top: 34px; font-size: 17px; }
  .card--front .practice-mark__dot { width: 10px; height: 10px; }
  .card--back .practice-mark { left: 118px; top: 104px; font-size: 28px; }
  .card--back .practice-mark__dot { width: 14px; height: 14px; }

  .doctor-name {
    position: absolute; left: 23px; top: 162px;
    font-size: 19px; font-weight: 600; color: var(--ink);
  }
  .doctor-specialty {
    position: absolute; left: 24px; top: 190px;
    font-size: 13px; font-weight: 500; color: var(--blue);
  }
  .contact-col {
    position: absolute; top: 238px;
    font-size: 11.6px; font-weight: 500; color: var(--blue); line-height: 15px;
    white-space: nowrap;
  }
  .contact-col--address { left: 24px; }
  .contact-col--phone { left: 178px; }
  .contact-col--web { left: 329px; }

  .back-website {
    position: absolute; left: 0; right: 0; top: 248px;
    text-align: center;
    font-size: 12.5px; font-weight: 500; color: var(--blue);
  }
</style>
</head>
<body>
  <section class="card card--front">
    <div class="practice-mark">
      <span class="practice-mark__dot"></span>
      <span class="practice-mark__name">Silver Birch<br>Retina Care</span>
    </div>
    <h1 class="doctor-name">Dr.Tobias Rendell (MD, PhD)</h1>
    <p class="doctor-specialty">Board-Certified Vitreoretinal Surgeon</p>
    <p class="contact-col contact-col--address">87 Larkspur Ave, Suite 210,<br>Needham MA 02481</p>
    <p class="contact-col contact-col--phone">Phone: 617-482 - 7730<br>Fax: 617-391-2268</p>
    <p class="contact-col contact-col--web">info@sbretinahub.example<br>www.sbretinahub.example</p>
  </section>

  <section class="card card--back">
    <div class="practice-mark">
      <span class="practice-mark__dot"></span>
      <span class="practice-mark__name">Silver Birch<br>Retina Care</span>
    </div>
    <p class="back-website">www.sbretinahub.example</p>
  </section>
</body>
</html>
```